Book Cover for: TITLE Mend the Quiet Hours SUBTITLE For couples who don't want to break up

We need a full cover design for a book on relationships written by husband and wife team, Marla and Walter Dunmore, PhD. This book will offer hope for couples that are on the verge of breaking up but want to work things out and stay together. The theme is to teach couples about their own reactions to their partner, how moods affect a relationship, how to get creative to solving problems and how to have a good feeling towards your partner regardless of differences. This book is about hope. It is a positive look at relationships that feel hopeless.

Target Market(s)

Married or couples that are going through a difficult time and are considering splitting up due to, communication difficulties, addiction, affair. We imagine the book will appeal to women more than men but still want a cover that men would be comfortable picking up.

Colors

Designer to choose colors to be used in the design.

Requirements
Must have
• We want the cover to beautiful, intriguing, simple and uncomplicated. We don't want it overly busy, technical, or complex.
Nice to have
• MAYBE?? a broken heart being put back together.
Should not have
• No photo, no cartoon, no flowers, no couple (unless obscure and not gender specific).

```html
<!DOCTYPE html>
<html lang="en">
<head>
<meta charset="utf-8">
<title>Mend the Quiet Hours — Book Cover</title>
<link href="https://fonts.googleapis.com/css2?family=EB+Garamond:wght@400;600;700;800&display=swap" rel="stylesheet">
<style>
  :root {
    --paper: #ecd8b4;
    --paper-light: #f1e0c1;
    --paper-shade: #e2c99f;
    --title-red: #b8111a;
    --heart-red: #b40608;
    --heart-deep: #9a0306;
    --ink: #141010;
  }
  html, body {
    margin: 0;
    padding: 0;
    width: 927px;
    height: 1200px;
    overflow: hidden;
  }
  .cover {
    position: relative;
    width: 927px;
    height: 1200px;
    background: radial-gradient(ellipse at 50% 40%, var(--paper-light) 0%, var(--paper) 55%, var(--paper-shade) 100%);
    font-family: "EB Garamond", Georgia, serif;
    text-align: center;
    overflow: hidden;
  }
  .title {
    position: absolute;
    top: 28px;
    left: 0;
    right: 0;
    margin: 0;
    color: var(--title-red);
    font-weight: 400;
    line-height: 1;
  }
  .title span { display: block; }
  .title-lead {
    position: relative;
    font-size: 128px;
    font-weight: 800;
    letter-spacing: 1px;
    height: 112px;
  }
  .title-middle {
    font-size: 104px;
    height: 96px;
    margin-top: 4px;
  }
  .title-main {
    font-size: 186px;
    height: 160px;
    letter-spacing: 2px;
  }
  .title-crack {
    position: absolute;
    top: 0;
    left: 0;
    width: 927px;
    height: 120px;
    pointer-events: none;
  }
  .heart-art {
    position: absolute;
    left: 105px;
    top: 424px;
    width: 710px;
    height: 523px;
    background: radial-gradient(ellipse 50% 50% at 50% 48%, var(--heart-red) 0%, var(--heart-deep) 55%, rgba(236, 216, 180, 0) 100%);
  }
  .subtitle {
    position: absolute;
    top: 972px;
    left: 0;
    right: 0;
    margin: 0;
    color: var(--ink);
    font-size: 50px;
    line-height: 57px;
    font-weight: 400;
  }
  .author {
    position: absolute;
    top: 1128px;
    left: 0;
    right: 0;
    margin: 0;
    color: var(--ink);
    font-size: 30px;
    font-weight: 700;
    letter-spacing: 2px;
  }
</style>
</head>
<body>
  <main class="cover">
    <h1 class="title">
      <span class="title-lead">MEND
        <svg class="title-crack" viewBox="0 0 927 120" aria-hidden="true">
          <polyline points="300,48 420,58 470,54 640,78" fill="none" stroke="var(--paper)" stroke-width="4"/>
        </svg>
      </span>
      <span class="title-middle">THE QUIET</span>
      <span class="title-main">HOURS</span>
    </h1>

    <div class="heart-art" role="img" aria-label="Photograph of a heart-shaped hole torn through cream paper, revealing deep red beneath"></div>

    <p class="subtitle">For couples who don't want to<br>break up</p>
    <p class="author">AUTHOR NAME</p>
  </main>
</body>
</html>
```